Visitenkarte erstellen für Reiki Praxis

Visitenkarten für Reiki Praxis Doppelseitig

business cards reiki practice double-sided

The background can also be a different color

```html
<!DOCTYPE html>
<html lang="en">
<head>
<meta charset="utf-8">
<title>Quiet Currents – Business Card</title>
<link rel="stylesheet" href="https://fonts.googleapis.com/css2?family=Raleway:wght@400;500;600&display=swap">
<style>
  :root {
    --page-bg: #e9e4de;
    --card-light-top: #f6f3f0;
    --card-light-bottom: #ecdfe0;
    --card-dark: #0c0c0c;
    --card-dark-soft: #1c1c1c;
    --accent-orange: #d9822f;
    --accent-plum: #7a2f5a;
    --gold: #c98a2c;
    --text-dark: #3a3a3a;
    --brand-light: #d9d2c6;
  }
  * { box-sizing: border-box; margin: 0; padding: 0; }
  html, body {
    width: 1200px;
    height: 969px;
    overflow: hidden;
    background: var(--page-bg);
    font-family: "Raleway", sans-serif;
  }
  .business-card {
    position: absolute;
    left: 160px;
    top: 234px;
    width: 880px;
    height: 500px;
    border-radius: 22px;
    overflow: hidden;
    box-shadow: 0 18px 40px rgba(0,0,0,0.18);
  }
  .card-shapes { position: absolute; inset: 0; }
  .contact-panel { position: absolute; left: 55px; top: 0; color: var(--text-dark); }
  .holder-name {
    position: absolute; top: 160px; left: 0;
    font-size: 28px; font-weight: 600; color: var(--accent-plum);
    white-space: nowrap; letter-spacing: 0.3px;
  }
  .holder-title {
    position: absolute; top: 196px; left: 0;
    font-size: 18px; font-weight: 500; color: var(--gold);
  }
  .address-line, .contact-line {
    position: absolute; left: 0;
    font-size: 19px; white-space: nowrap;
  }
  .address-line.first { top: 232px; }
  .address-line.second { top: 257px; }
  .contact-line { padding-left: 25px; }
  .contact-line.phone { top: 294px; }
  .contact-line.email { top: 319px; }
  .contact-line.web { top: 344px; }
  .contact-icon { position: absolute; left: 0; top: 6px; width: 14px; height: 14px; }
  .brand-block {
    position: absolute; left: 430px; right: 0; top: 258px;
    text-align: center;
  }
  .brand-name {
    font-size: 30px; font-weight: 500; color: var(--brand-light);
    letter-spacing: 1px;
  }
  .brand-owner {
    margin-top: 0px;
    font-size: 20px; font-weight: 500; color: var(--gold);
    letter-spacing: 7px;
  }
</style>
</head>
<body>
  <div class="business-card">
    <svg class="card-shapes" viewBox="0 0 880 500" width="880" height="500" aria-hidden="true">
      <defs>
        <linearGradient id="lightSide" x1="0" y1="0" x2="0.3" y2="1">
          <stop offset="0" stop-color="var(--card-light-top)"/>
          <stop offset="1" stop-color="var(--card-light-bottom)"/>
        </linearGradient>
        <linearGradient id="darkSide" x1="0" y1="0" x2="1" y2="1">
          <stop offset="0" stop-color="var(--card-dark)"/>
          <stop offset="0.6" stop-color="var(--card-dark)"/>
          <stop offset="1" stop-color="var(--card-dark-soft)"/>
        </linearGradient>
      </defs>
      <rect class="light-side" width="880" height="500" fill="url(#lightSide)"/>
      <path class="wave-edge-orange" d="M390,0 C344,30 324,90 344,170 C364,250 444,300 429,380 C419,440 394,480 364,500"
            fill="none" stroke="var(--accent-orange)" stroke-width="5"/>
      <path class="wave-edge-plum" d="M394,0 C348,30 328,90 348,170 C368,250 448,300 433,380 C423,440 398,480 368,500"
            fill="none" stroke="var(--accent-plum)" stroke-width="5"/>
      <path class="dark-side" d="M398,0 C352,30 332,90 352,170 C372,250 452,300 437,380 C427,440 402,480 372,500 L880,500 L880,0 Z"
            fill="url(#darkSide)"/>
    </svg>

    <div class="contact-panel">
      <div class="holder-name">DANIEL REED</div>
      <div class="holder-title">President</div>
      <div class="address-line first">4120 Willow Crest Road</div>
      <div class="address-line second">Fairbanks, Alaska 99701</div>
      <div class="contact-line phone">
        <svg class="contact-icon" viewBox="0 0 14 14"><path d="M3 1 L5.5 1 L6.5 4 L5 5.2 C5.8 7 7 8.2 8.8 9 L10 7.5 L13 8.5 L13 11 C13 12 12 13 11 13 C5.5 12.5 1.5 8.5 1 3 C1 2 2 1 3 1 Z" fill="var(--gold)"/></svg>
        555-014-2238
      </div>
      <div class="contact-line email">
        <svg class="contact-icon" viewBox="0 0 14 14"><rect x="1" y="3" width="12" height="8.5" rx="1" fill="var(--gold)"/><path d="M1.5 3.5 L7 8 L12.5 3.5" fill="none" stroke="#fff" stroke-width="1"/></svg>
        info@QuietCurrents.com
      </div>
      <div class="contact-line web">
        <svg class="contact-icon" viewBox="0 0 14 14"><circle cx="7" cy="7" r="6" fill="var(--gold)"/><path d="M1 7 H13 M7 1 C4 4 4 10 7 13 M7 1 C10 4 10 10 7 13" fill="none" stroke="#fff" stroke-width="0.8"/></svg>
        QuietCurrents.com
      </div>
    </div>

    <div class="brand-block">
      <div class="brand-name">QUIET CURRENTS</div>
      <div class="brand-owner">MARA LENZ</div>
    </div>
  </div>
</body>
</html>
```